LUNA VELADA

Luna Velada is a tribute to the hidden treasures of Chile’s majestic mountain landscapes. Each bottle captures the essence of the Andes, where rugged peaks and fertile valleys create the perfect harmony for winemaking. With a label inspired by the mystique of the mountains, Luna Velada invites you to uncover the rich flavors and stories hidden within its depths—a wine as bold and timeless as the land it comes from. the current design is old and not attractiv at all we want something new
Updates

Please create a mysterious, enigmatic label based on the typography and logo attached to the project. We need at least, at the entry level, five varietal products such as Carménère, Cabernet Sauvignon, Merlot, Chardonnay, and Malbec. Later, we would like to add more premium products, like a Reserva, a Special Reserva, or a Limited Edition. The design should be flexible and easily adaptable to accommodate various products while maintaining the same overall aesthetic.

Project Brief – Large-Scale Brand Label Design
We are developing a new large-scale brand with a structured range of wines. Below are the key design elements and specifications for the labels:

Entry-Level Wines (Bordeaux Bottle Shape)
Varietals: Cabernet Sauvignon, Carménère, Merlot, Cabernet-Merlot, Sauvignon Blanc.
Do not mention the word "varietals" on the label.
Next Level – Special Reserve (Burgundy Bottle Shape)
Varietals: Pinot Noir, Chardonnay, Syrah.
The label must include the mention "Special Reserve."
Premium Level – Limited (Heavy Conical Bottle Shape)
Varietal: Carménère-Malbec.
The label must include the mention "Limited."
Top Level – Secret Blend (Heavy Conical Bottle Shape)
Name on the label: "Secret Blend."
General Label Guidelines
Year: Only mention "2024" (do not include the word “vintage”).
Capsules: Use standard-colored capsules only (no branding).
Design Concept: The style should align with our brand identity. Please refer to www.marlonde-vins.example for inspiration and coherence.

Target Market(s)

younger generation,

Industry/Entity Type

Wines producer

Requirements
Must have
• the original logo with the name it is register We need to indicate the varietals Cabernet Sauvignon, the vintage 2024, the region DO Central Valley
Nice to have
• one white wines version of the label on a burgendy bottle shape and one red wines label on bordeau bottles sahpe

```html
<!DOCTYPE html>
<html lang="en">
<head>
<meta charset="utf-8">
<title>Luna Velada – Special Reserve Labels</title>
<link href="https://fonts.googleapis.com/css2?family=Cinzel:wght@400;600;700&family=Lora:wght@400;700&display=swap" rel="stylesheet">
<style>
  :root {
    --bg: #ffffff;
    --paper: #fbf8ee;
    --ink: #1d1b18;
    --stone: #8f8c76;
    --stone-light: #c9c6b3;
    --gold: #d4a52b;
    --gold-light: #ecd08a;
    --crimson: #b0171f;
    --crimson-light: #de7b7f;
  }
  * { box-sizing: border-box; margin: 0; padding: 0; }
  html, body { width: 1200px; height: 960px; overflow: hidden; background: var(--bg); }
  .range { position: relative; width: 1200px; height: 960px; }

  .label {
    position: absolute; top: 250px; width: 330px; height: 460px;
    background: var(--paper);
    clip-path: polygon(0 60px, 125px 66px, 290px 0, 100% 10px, 100% 100%, 0 100%);
    box-shadow: 0 0 0 1px rgba(0,0,0,.04);
    color: var(--ink);
  }
  .label--stone { left: 75px; --accent: var(--stone); --accent-light: var(--stone-light); }
  .label--gold { left: 435px; --accent: var(--gold); --accent-light: var(--gold-light); }
  .label--crimson { left: 795px; --accent: var(--crimson); --accent-light: var(--crimson-light); }

  .label__landscape {
    position: absolute; left: 0; top: 0; width: 100%; height: 175px;
    background: linear-gradient(180deg, var(--paper) 0%, var(--accent-light) 40%, var(--accent) 100%);
  }

  .label__title {
    position: absolute; top: 190px; left: 0; width: 100%;
    font-family: "Cinzel", serif; font-weight: 700; font-size: 44px;
    line-height: 48px; text-align: center; letter-spacing: -1px;
  }

  .label__tier {
    position: absolute; top: 300px; left: 0; width: 100%;
    text-align: center; font-family: "Lora", serif; font-size: 13px; line-height: 15px;
  }
  .label__tier-name { color: var(--accent); font-weight: 700; letter-spacing: .5px; }
  .label__grape { letter-spacing: .5px; }

  .label__tree {
    position: absolute; top: 292px; left: 42px; width: 40px; height: 44px;
    background: var(--accent); opacity: .75; border-radius: 50% 50% 8px 8px;
  }

  .label__origin {
    position: absolute; top: 342px; left: 0; width: 100%; text-align: center;
    font-family: "Lora", serif; font-size: 10px; letter-spacing: 2.5px;
  }

  .label__rule {
    position: absolute; top: 358px; left: 25px; right: 25px; height: 4px;
    border-top: 1.5px solid var(--accent); border-bottom: 1px solid var(--accent);
  }

  .label__house {
    position: absolute; top: 368px; left: 25px; right: 25px; height: 46px;
    background: var(--accent); display: flex; align-items: center; justify-content: center;
  }
  .label__house::after {
    content: ""; position: absolute; inset: 4px; border: 1px solid var(--paper);
  }
  .label__house-name {
    font-family: "Cinzel", serif; font-weight: 400; font-size: 17px;
    color: var(--paper); letter-spacing: 1px;
  }

  .label__since {
    position: absolute; top: 424px; left: 0; width: 100%; text-align: center;
    font-family: "Lora", serif; font-size: 8px; letter-spacing: 2px;
  }
</style>
</head>
<body>
<main class="range">

  <article class="label label--stone">
    <div class="label__landscape" role="img" aria-label="Engraved Andes mountain landscape in stone grey"></div>
    <h1 class="label__title">LUNA<br>VELADA</h1>
    <div class="label__tree" role="img" aria-label="Small engraved tree"></div>
    <p class="label__tier"><span class="label__tier-name">SPECIAL RESERVE</span><br><span class="label__grape">PINOT NOIR</span></p>
    <p class="label__origin">WINE OF CHILE</p>
    <div class="label__rule"></div>
    <div class="label__house"><span class="label__house-name">Familia Marlonde</span></div>
    <p class="label__since">SINCE 1880</p>
  </article>

  <article class="label label--gold">
    <div class="label__landscape" role="img" aria-label="Engraved Andes mountain landscape in golden tones"></div>
    <h1 class="label__title">LUNA<br>VELADA</h1>
    <p class="label__tier"><span class="label__tier-name">SPECIAL RESERVE</span><br><span class="label__grape">CHARDONNAY</span></p>
    <p class="label__origin">WINE OF CHILE</p>
    <div class="label__rule"></div>
    <div class="label__house"><span class="label__house-name">Familia Marlonde</span></div>
    <p class="label__since">SINCE 1880</p>
  </article>

  <article class="label label--crimson">
    <div class="label__landscape" role="img" aria-label="Engraved Andes mountain landscape in crimson tones"></div>
    <h1 class="label__title">LUNA<br>VELADA</h1>
    <div class="label__tree" role="img" aria-label="Small engraved tree"></div>
    <p class="label__tier"><span class="label__tier-name">SPECIAL RESERVE</span><br><span class="label__grape">PINOT NOIR</span></p>
    <p class="label__origin">WINE OF CHILE</p>
    <div class="label__rule"></div>
    <div class="label__house"><span class="label__house-name">Familia Marlonde</span></div>
    <p class="label__since">SINCE 1880</p>
  </article>

</main>
</body>
</html>
```